Connect With Your Target Audience and Sponsorship Levels Brochure

We need a brochure to print (with Printolux or similar firm) and give to possible sponsors.

it must describe the traffic and the sponsorship levels covered at:

http://www.korvane-guild.example/Sponsorship_Levels.html

4 pages
1. Our web sites from the

2 - 3. Sponsorship Levels from the

4. Have you got a better deal elsewhere?

We have tried hard to offer the best possible return for your investment in the Basel II / Basel III products and services industries.

We strongly believe this is a win-win opportunity. You will effectively promote your products and services, and connect with the members and friends of the association. Our members will benefit from your discounted offers. Our association will use the additional revenue to offer better services to all members.

To express your interest in becoming the silver sponsor of the association, please send an email to Mara Tolbeck at mara@korvane-guild.example

If we believe that your product or service is a good fit for our members and friends, we will send you a QuidRoute invoice for secure payment.

After the payment, in 2-5 business days we will develop your dedicated web page and we will start delivering what we have promised. Then we will send you an email informing you that we are ready, and we will start counting the 30 days of your sponsorship."

"To learn more:
Korvane Ledger Practitioners Guild (KLPG)
"
We have some other similar projects that follow.

Thank you.

We need a brochure to print (with Printolux or similar firm) and give to possible sponsors. 4 pages 1st page. Our web sites AND trafffic from the http://www.korvane-guild.example/Sponsorship_Levels.html 2nd page - 3rd page. Sponsorship Levels from the http://www.korvane-guild.example/Sponsorship_Levels.html 4. The text that follows: Have you got a better deal elsewhere? We have tried hard to offer the best possible return for your investment in the Basel II / Basel III products and services industries. We strongly believe this is a win-win opportunity. You will effectively promote your products and services, and connect with the members and friends of the association. Our members will benefit from your discounted offers. Our association will use the additional revenue to offer better services to all members. To express your interest in becoming the silver sponsor of the association, please send an email to Mara Tolbeck at mara@korvane-guild.example If we believe that your product or service is a good fit for our members and friends, we will send you a QuidRoute invoice for secure payment. After the payment, in 2-5 business days we will develop your dedicated web page and we will start delivering what we have promised. Then we will send you an email informing you that we are ready, and we will start counting the 30 days of your sponsorship." "To learn more: Korvane Ledger Practitioners Guild (KLPG) http://www.korvane-guild.example/Sponsorship_Levels.html " We have some other similar projects that follow. Thank you.

Industry/Entity Type

Investment

Colors
0255a3
ec1f27

```html
<!DOCTYPE html>
<html lang="en">
<head>
<meta charset="utf-8">
<title>Levels of Sponsorship</title>
<link href="https://fonts.googleapis.com/css2?family=Source+Sans+3:wght@400;700&family=Noto+Serif:wght@700&display=swap" rel="stylesheet">
<style>
:root{
  --brand-blue:#0255a3;
  --brand-red:#ec1f27;
  --ink:#2b2b2b;
  --paper:#ffffff;
}
*{margin:0;padding:0;box-sizing:border-box}
html,body{width:929px;height:1200px;overflow:hidden;background:var(--paper)}
.page{position:relative;width:929px;height:1200px;font-family:"Source Sans 3",sans-serif;color:var(--ink)}
.section-tab{position:absolute;left:0;top:474px;width:297px;height:157px;background:var(--brand-red);display:flex;align-items:center;padding-left:51px;padding-top:8px}
.section-tab h1{font-family:"Noto Serif",serif;font-weight:700;font-size:22px;line-height:29px;color:#fff}
.tier-art{position:absolute;left:348px;width:109px;height:172px;border-radius:4px}
.art-diamond{top:52px;background:radial-gradient(circle at 50% 50%,#9fd4ff 0,#2f7fe0 30%,#0b3d9c 70%,#061f5c 100%)}
.art-platinum{top:394px;background:radial-gradient(circle at 50% 50%,#f2f0f8 0,#9b97b3 35%,#4a4560 70%,#25213a 100%)}
.art-gold{top:626px;background:radial-gradient(circle at 50% 50%,#fff3c0 0,#e0a83a 35%,#b0601c 70%,#6a3410 100%)}
.art-silver{top:859px;background:radial-gradient(circle at 50% 50%,#ffffff 0,#c4c4c4 35%,#7a7a7a 70%,#3e3e3e 100%)}
.tier{position:absolute;left:478px;width:400px;font-size:14.3px;line-height:15.8px}
.tier h2{font-size:14.3px;font-weight:700;line-height:17px;color:#1e1e1e}
.tier .price{font-weight:700;line-height:18px;color:#1e1e1e}
.tier p{text-align:justify}
.tier ol{list-style:none;counter-reset:b}
.tier li{counter-increment:b;position:relative;padding-left:26px;text-align:justify;margin-top:2px}
.tier li::before{content:counter(b) ".";position:absolute;left:0}
.tier-diamond{top:53px}
.tier-platinum{top:394px}
.tier-gold{top:627px}
.tier-silver{top:860px}
.footer{position:absolute;left:0;top:1105px;width:929px;height:95px}
.footer svg{position:absolute;left:0;top:0}
.footer-text{position:absolute;left:51px;top:12px;color:#fff;font-size:14.5px;line-height:18px}
.footer-text strong{font-weight:700}
</style>
</head>
<body>
<div class="page">
  <div class="section-tab"><h1>Levels of<br>Sponsorship</h1></div>

  <div class="tier-art art-diamond" role="img" aria-label="Blue wireframe globe artwork labelled Diamond"></div>
  <section class="tier tier-diamond">
    <h2>DIAMOND SPONSOR</h2>
    <div class="price">($8,000 per month)</div>
    <p>Blue Diamond Sponsorship is reserved for one leading industry organization. There is only one Blue Diamond Sponsorship opportunity available.</p>
    <p>A flawless blue diamond is one of the most valuable gemstones in the world. We have designed our blue diamond sponsorship as one of the most valuable sponsorships in the world of Basel II and Basel III.</p>
    <p>The benefits associated with the Blue Diamond Sponsor level are:</p>
    <ol>
      <li>Web Site(s) Advertising (Banner Ad 600x300)</li>
      <li>Newsletter Advertising (Banner Ad 600x300)</li>
      <li>Social Media Advertising</li>
      <li>Unique Perks That Employees and Clients Love</li>
      <li>A dedicated web page for your organization. Search Engine Optimization (SEO) techniques to improve the visibility of this web page</li>
      <li>Sponsor Guest Posting</li>
    </ol>
  </section>

  <div class="tier-art art-platinum" role="img" aria-label="Platinum wireframe globe artwork labelled Platinum"></div>
  <section class="tier tier-platinum">
    <h2>PLATINUM SPONSOR</h2>
    <div class="price">$5,000 per month</div>
    <p>There are only two Platinum Sponsorship opportunities available.</p>
    <p>The benefits associated with the Platinum Sponsor level are:</p>
    <ol>
      <li>Web Site(s) Advertising (Banner Ad 300x300)</li>
      <li>Newsletter Advertising (Banner Ad 300x300)</li>
      <li>Social Media Advertising</li>
      <li>Unique Perks That Employees and Clients Love</li>
      <li>A dedicated web page for your organization. Search Engine Optimization (SEO) techniques to improve the visibility of this web page</li>
    </ol>
  </section>

  <div class="tier-art art-gold" role="img" aria-label="Gold wireframe globe artwork labelled Gold"></div>
  <section class="tier tier-gold">
    <h2>GOLD SPONSOR</h2>
    <div class="price">$3,000 per month</div>
    <p>There are only three Gold Sponsorship opportunities available</p>
    <p>The benefits associated with the Gold Sponsor level are:</p>
    <ol>
      <li>Web Site(s) Advertising (Banner Ad 250x250)</li>
      <li>Newsletter Advertising (Banner Ad 250x250)</li>
      <li>Social Media Advertising</li>
      <li>Unique Perks That Employees and Clients Love</li>
      <li>A dedicated web page for your organization. Search Engine Optimization (SEO) techniques to improve the visibility of this web page</li>
    </ol>
  </section>

  <div class="tier-art art-silver" role="img" aria-label="Silver wireframe globe artwork labelled Silver"></div>
  <section class="tier tier-silver">
    <h2>SILVER SPONSOR</h2>
    <div class="price">$1,500 per month</div>
    <p>The benefits associated with the Silver Sponsor level are:</p>
    <ol>
      <li>Web Site(s) Advertising (Banner Ad 250x125)</li>
      <li>Newsletter Advertising (Banner Ad 250x125)</li>
      <li>A dedicated web page for your organization. Search Engine Optimization (SEO) techniques to improve the visibility of this web page</li>
    </ol>
  </section>

  <footer class="footer">
    <svg width="929" height="95" viewBox="0 0 929 95">
      <defs>
        <linearGradient id="roomTone" x1="0" y1="0" x2="1" y2="1">
          <stop offset="0" stop-color="#c98a3c"/>
          <stop offset="0.5" stop-color="#7a3d17"/>
          <stop offset="1" stop-color="#3a1a0a"/>
        </linearGradient>
      </defs>
      <polygon points="0,0 569,0 550,95 0,95" fill="var(--brand-blue)"/>
      <polygon points="576,0 929,0 929,95 557,95" fill="url(#roomTone)" role="img" aria-label="Photo of a wood-panelled conference room with a long table"/>
    </svg>
    <div class="footer-text">
      <strong>Over 26,300 members and friends receive our newsletter</strong><br>
      Learn more at:<br>
      <strong>http://www.korvane-guild.example/Sponsorship_Levels.html</strong>
    </div>
  </footer>
</div>
</body>
</html>
```